QuoteMarlin.com Homepage Redesign

Create a new homepage design for our website QuoteMarlin.com. Our current experience is focused on auto insurance only. We would like to incorporate the ability to receive rate estimates for home insurance and bundled (home + auto) insurance in addition to auto. Home insurance will include home, renters and condo. The final design should inspire users to utilize our comparison tool.

Industry/Entity Type

Insurance (Auto & Home)

Number of Pages Required

1 page

Font styles to use
Other font styles liked:
• See Assets - Sans Serif & Roboto

Colors
0054AA
0677BA
7BADD7
CADEEF
E8F1F8
59FF00
82FF00
B8FF75
E3FFCB
F4FFEA

Requirements
Must have
• Must include the ability to launch our rate comparison tool within the main hero image for Auto, Home, Bundled.
Nice to have
• The design should be bold and eye catching. It should be differentiated from the typical landing page experience. (Some of our favorite sites from a UX perspective include: Vaultline.org, ThePelican.com, Ferrow.com and Corvane Airways - They are busy but we like the app like approach on the homepage)
Should not have
• We are not looking for a design that is heavy on generic images.

```html
<!DOCTYPE html>
<html lang="en">
<head>
<meta charset="utf-8">
<title>QuoteMarlin – Home page Redesign</title>
<link href="https://fonts.googleapis.com/css2?family=Inter:wght@400;500;600;700&family=Roboto:wght@300;400;500&display=swap" rel="stylesheet">
<style>
:root{
  --board:#0565f6;
  --brand:#0057e7;
  --ink:#1b1d22;
  --muted:#9a9ea8;
  --line:#dfe3ea;
  --band:#f3f4f6;
  --accent:#ffd39a;
  --white:#ffffff;
}
*{box-sizing:border-box;margin:0;padding:0}
html,body{width:1200px;height:900px;overflow:hidden}
body{background:var(--board);font-family:"Roboto",sans-serif;color:var(--ink);position:relative}
.brand-mark{position:absolute;left:47px;top:104px;display:flex;align-items:center;gap:10px;color:var(--white);font-family:"Inter",sans-serif;font-weight:600;font-size:30px;letter-spacing:-.3px}
.brand-mark .dot{width:30px;height:30px;border-radius:50%;background:var(--white)}
.board-title{position:absolute;left:46px;top:738px;color:var(--white);font-family:"Inter",sans-serif}
.board-title .small{font-size:27px;font-weight:500}
.board-title .big{font-size:56px;font-weight:600;letter-spacing:-1px;line-height:1.1}

.page{position:absolute;left:410px;top:76px;width:693px;height:824px;background:var(--white);border-radius:14px 14px 0 0;overflow:hidden;
  background-image:radial-gradient(circle at 20% 12%,#fff3e3 0,rgba(255,255,255,0) 40%),radial-gradient(circle at 95% 45%,#d6e5ff 0,rgba(255,255,255,0) 30%)}
.page *{position:absolute}
.page br{position:static}
.nav-logo{left:42px;top:10px;display:flex;align-items:center;gap:4px;font-family:"Inter",sans-serif;font-weight:600;font-size:10px;color:#12306b}
.nav-logo .dot{position:static;width:9px;height:9px;border-radius:2px;background:var(--brand)}
.nav-link{top:13px;font-size:6.8px;color:#2a2d33}
.nav-cta{left:593px;top:9px;width:60px;height:16px;border:1px solid var(--brand);border-radius:3px;color:var(--brand);font-size:6.8px;display:flex;align-items:center;justify-content:center}

.pill{background:var(--white);border-radius:10px;box-shadow:0 1px 4px rgba(0,0,0,.05);font-size:7.4px;color:#2a2d33;display:flex;align-items:center;gap:4px;padding:0 9px}
.pill i{position:static;font-style:normal;font-size:7px}
.hero-pill{left:42px;top:112px;height:18px}
.hero-title{left:42px;top:130px;width:300px;font-family:"Roboto",sans-serif;font-weight:400;font-size:24px;line-height:32px;color:#1e2024;white-space:nowrap}
.hero-title span{position:static;background:linear-gradient(transparent 62%,var(--accent) 62%,var(--accent) 88%,transparent 88%)}
.hero-copy{left:42px;top:234px;width:290px;font-size:9.3px;line-height:16px;color:var(--muted);font-weight:300;white-space:nowrap}
.btn-primary{left:42px;top:285px;width:109px;height:32px;background:var(--brand);border-radius:6px;color:var(--white);font-size:7.6px;font-weight:500;display:flex;align-items:center;justify-content:center;gap:10px}
.btn-primary .chev,.btn-form .chev{position:static;width:12px;height:12px;border-radius:50%;background:rgba(255,255,255,.25);display:flex;align-items:center;justify-content:center}
.link-play{left:178px;top:292px;display:flex;align-items:center;gap:6px;color:var(--brand);font-size:7.8px}
.link-play .play{position:static;width:19px;height:19px;border-radius:50%;background:#e4edff;display:flex;align-items:center;justify-content:center}

.quote-card{left:403px;top:62px;width:251px;height:277px;background:rgba(255,255,255,.92);border-radius:8px;box-shadow:0 6px 24px rgba(40,90,200,.12);overflow:hidden}
.quote-photo{left:70px;top:90px;width:140px;height:150px;border-radius:50%;background:radial-gradient(circle,#f6e6cf 0,rgba(255,255,255,0) 70%);opacity:.7}
.quote-card h2{left:17px;top:14px;font-weight:400;font-size:15.5px;color:#15171b}
.quote-card .sub{left:17px;top:37px;font-size:6.4px;color:var(--muted)}
.tabs{left:13px;top:56px;width:226px;height:20px;background:#eef2f8;border-radius:4px}
.tab{top:4px;height:13px;font-size:6.3px;color:#8a93a6;display:flex;align-items:center;padding:0 8px}
.tab.on{left:3px;background:var(--white);color:var(--brand);border-radius:3px;box-shadow:0 1px 2px rgba(0,0,0,.06)}
.lbl{font-size:7.3px;color:#22252b}
.toggle{width:27px;height:11px;border-radius:6px;font-size:4.6px;font-weight:600;display:flex;align-items:center}
.toggle.on{background:var(--brand);color:var(--white);padding-left:4px}
.toggle.on::after{content:"";position:absolute;right:1.5px;top:1.5px;width:8px;height:8px;border-radius:50%;background:var(--white)}
.toggle.off{background:#e9ebef;color:#8a8f99;padding-left:13px}
.toggle.off::after{content:"";position:absolute;left:1.5px;top:1.5px;width:8px;height:8px;border-radius:50%;background:var(--white)}
.field{height:17px;border:1px solid var(--line);border-radius:2px;background:var(--white);font-size:6.2px;color:#c2c6cf;display:flex;align-items:center;padding-left:4px}
.field svg{right:6px;top:5px}
.info{position:static !important;display:inline-block;width:5px;height:5px;border-radius:50%;background:#3b7cff;margin-left:2px}
.btn-form{left:21px;width:207px;height:32px;background:var(--brand);border-radius:6px;color:var(--white);font-size:7.4px;display:flex;align-items:center;justify-content:center;gap:8px}
.note{left:0;width:251px;top:261px;text-align:center;font-size:4.4px;color:#9aa0aa}

.partners{left:0;top:388px;width:693px;height:94px;background:var(--band)}
.partner{top:39px;font-family:"Inter",sans-serif;font-weight:600;font-size:11px;color:#a9adb5;white-space:nowrap}

.section-pill{left:264px;top:563px;height:18px}
.section-title{left:187px;top:596px;width:360px;font-weight:400;font-size:24px;line-height:32px;color:#1e2024}

.feature{border-radius:6px;overflow:hidden}
.feature.one{left:80px;top:698px;width:149px;height:140px;background:linear-gradient(160deg,#fff2e0 0,#eef1f8 60%,#c9d6ee 100%)}
.feature.two{left:270px;top:690px;width:149px;height:140px;background:linear-gradient(180deg,#fbe7cc 0,#fdf5ea 100%)}
.feature.three{left:460px;top:700px;width:149px;height:140px;background:linear-gradient(160deg,#c7d3ea 0,#f3f1ef 55%,#fde9cf 100%)}
.mock{left:37px;top:22px;width:75px;height:100px;background:var(--white);border-radius:5px;box-shadow:0 2px 8px rgba(0,0,0,.05)}
.badge{width:18px;height:18px;border-radius:50%;background:#2a2522;box-shadow:inset 0 0 0 5px #2a2522,inset 0 0 0 9px #e3a43f}
.bar{left:10px;height:6px;border-radius:3px;background:#eef0f3}
.mini-field{left:10px;width:55px;height:9px;border-radius:4px;background:#f0f1f4;font-size:3.6px;color:#b7bbc4;padding-left:5px;display:flex;align-items:center}
.feature.two h3{left:0;width:149px;top:53px;text-align:center;font-weight:500;font-size:10px;color:#1b1d22}
.feature.two p{left:12px;width:125px;top:75px;text-align:center;font-size:7.4px;line-height:9.8px;color:#3b3e45}
</style>
</head>
<body>

<div class="brand-mark"><span class="dot"></span>QuoteMarlin</div>

<div class="board-title">
  <div class="small">Home page</div>
  <div class="big">Redesign</div>
</div>

<main class="page">
  <div class="nav-logo"><span class="dot"></span>QuoteMarlin</div>
  <span class="nav-link" style="left:187px">Auto Insurance</span>
  <span class="nav-link" style="left:272px">Home Insurance</span>
  <span class="nav-link" style="left:361px">Life Insurance</span>
  <span class="nav-link" style="left:443px">Resources</span>
  <span class="nav-link" style="left:513px">About Us</span>
  <span class="nav-cta">Instant Quote</span>

  <div class="pill hero-pill"><i>🔥</i>Discover the power of QuoteMarlin</div>
  <h1 class="hero-title">Get instant rate estimates<br>for <span>Home &amp; Bundled</span><br>Insurance Packages</h1>
  <p class="hero-copy">Get instant rate estimates for Home and Bundled Insurance!<br>Discover our new feature for accurate and affordable Coverage.</p>
  <a class="btn-primary">Discover more <span class="chev"><svg width="5" height="6" viewBox="0 0 5 6"><path d="M1 .5 3.5 3 1 5.5" stroke="#fff" fill="none" stroke-width="1"/></svg></span></a>
  <a class="link-play"><span class="play"><svg width="6" height="7" viewBox="0 0 6 7"><path d="M0 0 6 3.5 0 7z" fill="#0057e7"/></svg></span>How it works</a>

  <section class="quote-card">
    <div class="quote-photo" role="img" aria-label="Soft faded photo of a family pet behind the form"></div>
    <h2>Get the rates instantly</h2>
    <p class="sub">See what you should pay at top companies near you</p>
    <div class="tabs">
      <span class="tab on">Bundled(Home + Auto)</span>
      <span class="tab" style="left:87px">Home Insurance</span>
      <span class="tab" style="left:148px">Auto Insurance</span>
    </div>
    <span class="lbl" style="left:21px;top:95px">Do you own a Home?</span>
    <span class="toggle on" style="left:21px;top:108px">YES</span>
    <span class="lbl" style="left:128px;top:95px">Do you own a Car?</span>
    <span class="toggle off" style="left:128px;top:108px">NO</span>

    <span class="lbl" style="left:21px;top:135px">How old are you ?</span>
    <span class="field" style="left:21px;top:147px;width:31px">Age</span>
    <span class="lbl" style="left:128px;top:135px">Zip code</span>
    <span class="field" style="left:128px;top:147px;width:40px">Zip code</span>

    <span class="lbl" style="left:21px;top:180px">Current Provider</span>
    <span class="field" style="left:21px;top:192px;width:79px">Current Provider<svg width="6" height="4" viewBox="0 0 6 4"><path d="M.5.5 3 3 5.5.5" stroke="#333" fill="none"/></svg></span>
    <span class="lbl" style="left:128px;top:180px">Credit Score<span class="info"></span></span>
    <span class="field" style="left:128px;top:192px;width:79px">Credit Score<svg width="6" height="4" viewBox="0 0 6 4"><path d="M.5.5 3 3 5.5.5" stroke="#333" fill="none"/></svg></span>

    <a class="btn-form" style="top:223px">Retrieve results <span class="chev"><svg width="5" height="6" viewBox="0 0 5 6"><path d="M1 .5 3.5 3 1 5.5" stroke="#fff" fill="none" stroke-width="1"/></svg></span></a>
    <p class="note">All fields are mandatory</p>
  </section>

  <section class="partners">
    <span class="partner" style="left:32px">Harbor Crest</span>
    <span class="partner" style="left:128px">Elmwood</span>
    <span class="partner" style="left:206px">Keystone Shield</span>
    <span class="partner" style="left:304px">Northpoint</span>
    <span class="partner" style="left:392px">Velmora</span>
    <span class="partner" style="left:476px">Forwardly</span>
    <span class="partner" style="left:566px">Calder Mutual</span>
    <span class="partner" style="left:658px">Hollowind</span>
  </section>

  <div class="pill section-pill"><i>⚡</i>Empowering Informed Decision-Making</div>
  <h2 class="section-title">Your Comprehensive Resource for Making the Right Choices</h2>

  <article class="feature one" role="img" aria-label="Illustration of a quote summary card">
    <div class="mock">
      <span class="badge" style="left:28px;top:10px"></span>
      <span class="bar" style="top:34px;width:55px;height:8px"></span>
      <span class="bar" style="top:50px;width:62px;height:4px"></span>
      <span class="bar" style="top:60px;width:62px;height:4px"></span>
      <span class="bar" style="top:70px;width:45px;height:4px"></span>
    </div>
  </article>

  <article class="feature two">
    <span class="badge" style="left:65px;top:24px"></span>
    <h3>More choices</h3>
    <p>Unlike other sites, our results are not limited to paid sponsors. Our results represent top carriers in your geographic area based on the total premiums written.</p>
  </article>

  <article class="feature three" role="img" aria-label="Illustration of a contact details form">
    <div class="mock">
      <span class="badge" style="left:28px;top:10px"></span>
      <span class="mini-field" style="top:36px">Email ID</span>
      <span class="mini-field" style="top:50px">Contact no</span>
      <span class="mini-field" style="top:64px">Address</span>
    </div>
  </article>
</main>

</body>
</html>
```